Graphic that shows our management philosophy and strategy

We need a graphic design that shows our management framework. Attached is my (poor) attempt at making this look good. Please refer to this file:

Please note that the other 3 files in the attachments are just examples of works that I think are visually appealing.

Up to five colors can be used but less is fine also. If colors are used, then please use ones that are close to the colors in the graphic. This graphic will be used to show employees how and why we are doing what we do.

If you could create the graphic in Powerpoint, that would be ideal, but am willing to take any graphic format if it looks great

Target Market(s)

Internal employees

Industry/Entity Type

Graphic Design

Requirements
Must have
• Must show a hierarchy vertically between the various levels
Nice to have
• Using a pyramid as the background structure might be nice
• The last 3 attachments are examples I found that I found visually attractive.

```html
<!DOCTYPE html>
<html lang="en">
<head>
<meta charset="utf-8">
<title>Management Framework</title>
<link href="https://fonts.googleapis.com/css2?family=Arimo:wght@400;700&display=swap" rel="stylesheet">
<style>
  :root{
    --orange:#f7941d;
    --orange-dark:#e07b0a;
    --blue:#1d5f8e;
    --teal:#0f9a8c;
    --green:#1fae6e;
    --navy:#1c3557;
    --white:#ffffff;
    --ink:#1c3557;
  }
  *{box-sizing:border-box;margin:0;padding:0}
  html,body{width:800px;height:1200px;overflow:hidden;background:var(--white);font-family:"Arimo",Arial,sans-serif}
  .framework{position:relative;width:800px;height:1200px}

  .level-tile{position:absolute;left:8px;width:200px;color:var(--white);text-align:center;
    clip-path:polygon(0 0,88% 0,100% 50%,88% 100%,0 100%);padding-right:20px;
    display:flex;flex-direction:column;align-items:center;justify-content:center}
  .level-tile svg{width:78px;height:78px;margin-bottom:8px}
  .level-name{font-weight:700;font-size:26px;line-height:1}
  .level-sub{font-size:13px;margin-top:4px}
  .tile-aspirations{top:21px;height:214px;background:var(--orange)}
  .tile-values{top:253px;height:214px;background:var(--blue)}
  .tile-strategy{top:487px;height:212px;background:var(--teal)}
  .tile-metrics{top:717px;height:203px;background:var(--orange)}
  .tile-initiative{top:935px;height:252px;background:var(--navy)}

  .panel{position:absolute;left:232px;width:556px;color:var(--white)}
  .panel-aspirations{top:21px;height:214px;background:var(--orange);
    clip-path:polygon(0 0,100% 0,100% 100%,94% 100%,88% 88%,0 88%);padding:14px}
  .goals{display:grid;grid-template-columns:repeat(4,1fr);gap:10px}
  .goal-head{background:var(--white);color:var(--orange-dark);font-weight:700;font-size:22px;text-align:center;padding:6px 0}
  .goal-body{font-size:15px;font-weight:700;line-height:1.15;padding:10px 4px 0 18px;position:relative}
  .goal-body::before{content:"";position:absolute;left:2px;top:13px;width:10px;height:10px;background:var(--white)}

  .panel-values{top:253px;height:214px;background:var(--blue);display:flex;align-items:center;justify-content:space-around;padding:0 10px}
  .value{display:flex;flex-direction:column;align-items:center;width:125px;text-align:center}
  .value-label{font-weight:700;font-size:18px;line-height:1.1;margin-bottom:8px;min-height:40px;display:flex;align-items:flex-end}
  .value-disc{width:100px;height:100px;border-radius:50%;background:var(--white);color:var(--ink);
    display:flex;align-items:center;justify-content:center;font-weight:700;font-size:19px;line-height:1.05;padding:12px}
  .value-disc.small-text{font-size:16px}
  .value-disc svg{width:64px;height:64px}

  .panel-strategy{top:487px;height:212px;background:var(--teal);padding:18px 0 0 14px}
  .strategy-arrow{background:var(--green);font-size:19px;line-height:1.25;padding:10px 50px 10px 16px;margin-bottom:14px;
    clip-path:polygon(0 0,93% 0,100% 50%,93% 100%,0 100%);border-left:6px solid var(--white)}
  .strategy-arrow b{font-weight:700}

  .panel-metrics{top:717px;height:203px;background:var(--orange);padding:14px 18px}
  .metric{font-size:15px;line-height:1.2}
  .metric b{font-size:25px;font-weight:700}
  .metrics-chart{position:absolute;right:22px;bottom:22px;width:120px;height:100px}

  .panel-initiative{top:935px;height:252px;background:var(--navy);padding:16px 20px}
  .initiatives{list-style:none}
  .initiatives li{font-weight:700;font-size:19px;line-height:1.48;padding-left:18px;position:relative}
  .initiatives li::before{content:"";position:absolute;left:0;top:11px;width:8px;height:8px;border-radius:50%;background:var(--white)}
</style>
</head>
<body>
<main class="framework">

  <div class="level-tile tile-aspirations">
    <svg viewBox="0 0 80 80" fill="#fff" aria-hidden="true">
      <circle cx="20" cy="22" r="8"/><rect x="12" y="33" width="16" height="30" rx="4"/>
      <circle cx="40" cy="18" r="9"/><rect x="31" y="30" width="18" height="36" rx="4"/>
      <circle cx="60" cy="22" r="8"/><rect x="52" y="33" width="16" height="30" rx="4"/>
    </svg>
    <span class="level-name">Aspirations</span><span class="level-sub">Why we are here</span>
  </div>
  <div class="level-tile tile-values">
    <svg viewBox="0 0 80 80" fill="#fff" aria-hidden="true">
      <circle cx="22" cy="24" r="9"/><circle cx="58" cy="24" r="9"/><circle cx="40" cy="44" r="9"/>
      <rect x="30" y="56" width="20" height="18" rx="4"/>
    </svg>
    <span class="level-name">Values</span><span class="level-sub">How we act</span>
  </div>
  <div class="level-tile tile-strategy">
    <svg viewBox="0 0 80 80" fill="none" stroke="#fff" stroke-width="5" aria-hidden="true">
      <circle cx="38" cy="42" r="30"/><circle cx="38" cy="42" r="19"/><circle cx="38" cy="42" r="7" fill="#fff"/>
      <path d="M38 42 L70 10 M60 10h10v10"/>
    </svg>
    <span class="level-name">Strategy</span><span class="level-sub">How we succeed</span>
  </div>
  <div class="level-tile tile-metrics">
    <svg viewBox="0 0 80 80" fill="none" stroke="#fff" stroke-width="5" aria-hidden="true">
      <rect x="10" y="8" width="60" height="64" rx="4"/>
      <path d="M22 42l10 10 22-24"/>
    </svg>
    <span class="level-name">Metrics</span><span class="level-sub">What we measure</span>
  </div>
  <div class="level-tile tile-initiative">
    <svg viewBox="0 0 80 80" fill="#fff" aria-hidden="true">
      <path d="M40 8a22 22 0 0 0-13 40c3 3 4 6 4 10h18c0-4 1-7 4-10A22 22 0 0 0 40 8z"/>
      <rect x="31" y="61" width="18" height="5" rx="2"/><rect x="33" y="69" width="14" height="5" rx="2"/>
    </svg>
    <span class="level-name">Initiative</span><span class="level-sub">What we do</span>
  </div>

  <section class="panel panel-aspirations">
    <div class="goals">
      <div><div class="goal-head">Purpose</div><p class="goal-body">Power Solar Forward</p></div>
      <div><div class="goal-head">Vision</div><p class="goal-body">A World with Solar on every rooftop</p></div>
      <div><div class="goal-head">Purpose</div><p class="goal-body">Help installers become solar heroes</p></div>
      <div><div class="goal-head">Goal</div><p class="goal-body">Lead every market we participate in</p></div>
    </div>
  </section>

  <section class="panel panel-values">
    <div class="value"><span class="value-label">&nbsp;</span><div class="value-disc">Be One Team</div></div>
    <div class="value"><span class="value-label">Do The Right Thing</span>
      <div class="value-disc"><svg viewBox="0 0 64 64" fill="none" stroke="#1c3557" stroke-width="9" aria-hidden="true"><path d="M10 34l14 14 30-32"/></svg></div></div>
    <div class="value"><span class="value-label">Embrace Change</span>
      <div class="value-disc"><svg viewBox="0 0 64 64" fill="none" stroke="#1c3557" stroke-width="6" aria-hidden="true"><path d="M12 30a20 20 0 0 1 36-10M52 34a20 20 0 0 1-36 10"/><path d="M48 8v12H36M16 56V44h12"/></svg></div></div>
    <div class="value"><span class="value-label">&nbsp;</span><div class="value-disc small-text">Produce More With Less</div></div>
  </section>

  <section class="panel panel-strategy">
    <p class="strategy-arrow"><b>Target</b> quality-minded installers with configurable platform sold through distribution partners</p>
    <p class="strategy-arrow"><b>Target</b> larger, national installers with rail-less platform and direct sales and logistics support</p>
  </section>

  <section class="panel panel-metrics">
    <p class="metric"><b>People</b> Statification, Recruiting.</p>
    <p class="metric"><b>Products</b> Schedule, Quality.</p>
    <p class="metric"><b>Costumers</b> Share, Growth.</p>
    <p class="metric"><b>Service</b> Installer Sat, Partner Sat.</p>
    <p class="metric"><b>Operations</b> Margin, Cash.</p>
    <svg class="metrics-chart" viewBox="0 0 120 100" aria-hidden="true">
      <circle cx="60" cy="50" r="48" fill="#fff"/>
      <g fill="#f7941d"><rect x="30" y="58" width="12" height="22"/><rect x="48" y="46" width="12" height="34"/><rect x="66" y="36" width="12" height="44"/><rect x="84" y="26" width="10" height="54"/></g>
      <path d="M26 52 L50 36 L66 42 L92 18" fill="none" stroke="#1c3557" stroke-width="4"/>
    </svg>
  </section>

  <section class="panel panel-initiative">
    <ul class="initiatives">
      <li>Build out precense in key solar markets</li>
      <li>Extend platform with roof attachment</li>
      <li>Optimize existing components for cost</li>
      <li>Establish relationships with installers</li>
      <li>Launch fastest RL platform</li>
      <li>Develop KT-based flat roof solution</li>
      <li>Understand our business &amp; market better</li>
      <li>Divest ourselves of Brantley business</li>
    </ul>
  </section>

</main>
</body>
</html>
```